Harborview Tap & Grille Menu Makeover

I am looking for a professional look to update our current menu. We are an independently owned sports bar and grill. Up to this point, I have done all of my own graphic designing. I am looking for something classy/family oriented. We are a very family friendly sports bar that offers a wide variety of menu options. Our website is www.harborviewtapgrille.example. This may help you get more of a feel for what type of place we are and what we offer. Our menu is listed on the website. My current menu is 8.5x14 inserts that feature a cover page, 4 inside pages and a back page. I would like something a little more condensed than this. Possibly a large tri-fold menu? I am open to all new ideas. I do have some pictures on my menu now, and would like to continue using a few pictures to feature some of my items. I would like something that is in a format that gives me the option to change items and prices on my own in the future. I would also like it to feature, or inform my patrons about our technology that we offer. We offer online ordering and we are a "verified venue" with Brewlogr.( a social site for craft beer lovers).

Industry/Entity Type

Sports Bar

Requirements
Nice to have
• Nice to have some pictures, but does not have to. We do feature 9 different beers on tap. A lot of them are local craft beers from the state of Kansas. Not sure if that is something we can feature, but it is a nice talking point. All of our tables and bar are hand built. With a rich mahogany finish on all of our woodwork, some type of "woodgrain" look into the menu would be nice.

```html
<!DOCTYPE html>
<html lang="en">
<head>
<meta charset="utf-8">
<title>Harborview Tap &amp; Grille – Menu</title>
<link href="https://fonts.googleapis.com/css2?family=Audiowide&family=Arimo:wght@400;700&display=swap" rel="stylesheet">
<style>
  :root {
    --wood-dark: #23150e;
    --wood-mid: #3d271b;
    --wood-light: #4c3122;
    --banner-red: #e3212b;
    --text-white: #ffffff;
    --text-soft: #f1ebe6;
  }
  * { box-sizing: border-box; margin: 0; padding: 0; }
  html, body { width: 1200px; height: 848px; overflow: hidden; }
  body {
    position: relative;
    font-family: "Arimo", Arial, sans-serif;
    color: var(--text-white);
    background: var(--wood-dark);
  }
  .wood-backdrop {
    position: absolute; inset: 0;
    background: linear-gradient(90deg, var(--wood-dark) 0%, var(--wood-mid) 30%, var(--wood-light) 50%, var(--wood-mid) 72%, var(--wood-dark) 100%);
  }
  .menu-column { position: absolute; }
  .col-left { left: 14px; top: 0; width: 370px; }
  .col-mid { left: 414px; top: 0; width: 372px; }
  .col-right { left: 815px; top: 0; width: 362px; }

  .section-banner {
    position: absolute;
    height: 30px;
    background: var(--banner-red);
    font-family: "Audiowide", sans-serif;
    font-size: 25px;
    line-height: 31px;
    letter-spacing: 0.5px;
    color: var(--text-white);
  }
  .banner-appetizers { left: 0; top: 12px; width: 286px; padding-left: 38px; }
  .banner-salads { left: 0; top: 524px; width: 286px; padding-left: 38px; }
  .banner-entrees { left: 400px; top: 285px; width: 382px; padding-left: 58px; }
  .banner-sandwiches { left: 799px; top: 193px; width: 286px; padding-left: 58px; }

  .section-note { font-size: 8.5px; color: var(--text-soft); margin-bottom: 12px; }

  .menu-item { margin-bottom: 8px; }
  .item-head {
    display: flex; justify-content: space-between; align-items: baseline;
    font-weight: 700; font-size: 9.5px; line-height: 12px;
  }
  .item-price { font-size: 11px; font-weight: 400; }
  .item-desc { font-size: 7.4px; line-height: 9px; color: var(--text-soft); max-width: 345px; }
  .item-sizes { font-size: 10.5px; font-weight: 700; margin-top: 7px; word-spacing: 1px; }
  .item-sizes span { margin-right: 26px; }
  .item-sizes b { font-weight: 700; margin-left: 10px; }

  .appetizer-list { position: absolute; top: 52px; }
  .appetizer-list .menu-item { margin-bottom: 7.6px; }
  .salad-list { position: absolute; top: 556px; width: 370px; }
  .salad-list .section-note { margin-left: 24px; margin-bottom: 14px; }
  .salad-list .menu-item { margin-bottom: 11px; }

  .mid-salads { position: absolute; top: 15px; width: 372px; }
  .mid-salads .menu-item { margin-bottom: 11px; }
  .entree-list { position: absolute; top: 319px; width: 372px; }
  .entree-list .section-note { margin-left: 44px; margin-bottom: 8px; }
  .entree-list .menu-item { margin-bottom: 13px; }

  .steak-list { position: absolute; top: 15px; width: 362px; }
  .steak-list .menu-item { margin-bottom: 9px; }
  .sandwich-list { position: absolute; top: 227px; width: 362px; }
  .sandwich-list .section-note { margin-left: 42px; margin-bottom: 11px; }
  .sandwich-list .menu-item { margin-bottom: 10.4px; }
</style>
</head>
<body>
<div class="wood-backdrop" role="img" aria-label="Rich mahogany woodgrain background"></div>

<h2 class="section-banner banner-appetizers">APPETIZERS</h2>
<h2 class="section-banner banner-salads">SALADS</h2>
<h2 class="section-banner banner-entrees">ENTREES</h2>
<h2 class="section-banner banner-sandwiches">SANDWICHES</h2>

<section class="menu-column col-left">
  <div class="appetizer-list">
    <div class="menu-item"><div class="item-head"><span>Slider Burgers</span><span class="item-price">$8.99</span></div><p class="item-desc">Six Juicy bite sized burgers topped with American cheese and served with pickle slices</p></div>
    <div class="menu-item"><div class="item-head"><span>Loaded Potato Skins</span><span class="item-price">$8.99</span></div><p class="item-desc">Six crispy skins loaded with jack, cheddar and mozzarella cheese, then topped with smoked bacon and green onions. Served with sour cream</p></div>
    <div class="menu-item"><div class="item-head"><span>Rattlesnake Eggs</span><span class="item-price">$7.99</span></div><p class="item-desc">A spicy combo of pepper jack cheese and jalapeños, battered and fried</p></div>
    <div class="menu-item"><div class="item-head"><span>Mozzarella Cheese Sticks</span><span class="item-price">$7.99</span></div><p class="item-desc">Classic battered mozzarella cheese sticks. Served with ranch dressing.</p></div>
    <div class="menu-item"><div class="item-head"><span>Grand Slam French Fries</span><span class="item-price">$7.99</span></div><p class="item-desc">French fries loaded with jack, cheddar, mozzarella, bacon, jalapeños and green onions! Served with ranch dressing.</p></div>
    <div class="menu-item"><div class="item-head"><span>Bang Bang Shrimp</span><span class="item-price">$9.99</span></div><p class="item-desc">Lightly breaded and fried shrimp coated with a spicy Thai sauce, topped with parmesan cheese and diced tomatoes. Served over a bed of romaine lettuce.</p></div>
    <div class="menu-item"><div class="item-head"><span>Spicy Southwest Chicken Eggrolls</span><span class="item-price">$9.99</span></div><p class="item-desc">Stuffed with black beans, corn and chicken. Served with southwest ranch.</p></div>
    <div class="menu-item"><div class="item-head"><span>Blooming Onion</span><span class="item-price">$7.99</span></div><p class="item-desc">This fan favorite is classically carved and deep fried to perfection. Served with Harborview signature dipping sauce</p></div>
    <div class="menu-item"><div class="item-head"><span>Chicken Quesadilla</span><span class="item-price">$8.99</span></div><p class="item-desc">A 12 inch flour tortilla stuffed with grilled chicken and jack and cheddar cheese. Served with salsa</p></div>
    <div class="menu-item"><div class="item-head"><span>Ballpark Pretzel Basket</span><span class="item-price">$7.99</span></div><p class="item-desc">Buttered and salted pretzels served with Nacho cheese sauce.</p></div>
    <div class="menu-item"><div class="item-head"><span>Hank's Boneless Buffalo Wings</span><span class="item-price">$9.99</span></div><p class="item-desc">A full pound of spicy, boneless buffalo wings. Served with ranch dressing or Hank's Gold Label sauce.</p></div>
    <div class="menu-item"><div class="item-head"><span>Harborview Loaded Nachos</span><span class="item-price">$9.99</span></div><p class="item-desc">Tri-colored tortilla chips smothered with creamy monterey jack cheese, choice of beef or chicken, and topped with grilled peppers and onions, jalapeños and diced tomatoes. Served with sour cream and salsa.</p></div>
    <div class="menu-item"><div class="item-head"><span>Garlic Bread Basket</span><span class="item-price">$6.99</span></div><p class="item-desc">Eight buttered and garlic slices of Italian bread, lightly toasted. Served with marinara.</p></div>
  </div>

  <div class="salad-list">
    <p class="section-note">All Salads are served with garlic bread.</p>
    <div class="menu-item"><div class="item-head"><span>Chicken Tender Garden Salad</span><span class="item-price">$7.99 - $8.99</span></div><p class="item-desc">A Spring lettuce mix topped with shredded jack and cheddar cheese, garden vegetables, bacon, croutons and egg. With your choice of crispy or grilled chicken.</p><p class="item-sizes"><span>Small</span>$7.99 <b>Large</b> $8.99</p></div>
    <div class="menu-item"><div class="item-head"><span>Nacho Crunchito Salad</span><span class="item-price">$7.99 - $8.99</span></div><p class="item-desc">Harborview' unique blend of iceberg lettuce, topped with jack and cheddar cheese, tomatoes, black olives, ranch style beans and creamy Italian dressing. Topped with Crunchito Chips</p><p class="item-sizes"><span>Small</span>$7.99 <b>Large</b> $8.99</p></div>
    <div class="menu-item"><div class="item-head"><span>Cobb Salad</span><span class="item-price">$7.99 - $8.99</span></div><p class="item-desc">Rows of ham, turkey and roast beef, side by side with baby corn, jack and cheddar cheese, egg slices, garden vegetables, bacon and croutons served over iceberg lettuce.</p><p class="item-sizes"><span>Small</span>$7.99 <b>Large</b> $8.99</p></div>
    <div class="menu-item"><div class="item-head"><span>Summer Berry Salad</span><span class="item-price">$7.99 - $8.99</span></div><p class="item-desc">A blend of fresh berries, tomatoes, croutons, mandarin oranges and crumbled feta cheese served on fresh spinach leaves. Your choice of chicken or shrimp</p><p class="item-sizes"><span>Small</span>$7.99 <b>Large</b> $8.99</p></div>
  </div>
</section>

<section class="menu-column col-mid">
  <div class="mid-salads">
    <div class="menu-item"><div class="item-head"><span>House Caesar Salad</span><span class="item-price">$5.99 - $8.99</span></div><p class="item-desc">A classic mix of crisp romaine lettuce, shredded parmesan cheese, and croutons. Served with our signature Caesar dressing.</p><p class="item-sizes"><span>Small</span>$5.99 <b>Large</b> $6.99</p><p class="item-sizes" style="margin-top:6px"><span>Large With Chicken</span>$8.99 <b>Small With Chicken</b> &nbsp;&nbsp;$6.99</p></div>
    <div class="menu-item"><div class="item-head"><span>Napa Valley Salad</span><span class="item-price">$7.99 - $8.99</span></div><p class="item-desc">Fresh romaine lettuce blended with tomatoes, cranberries, walnuts, mandarin oranges, blue cheese crumbles and croutons. With your choice of grilled chicken or shrimp.</p><p class="item-sizes"><span>Small</span>$7.99 <b>Large</b> $8.99</p></div>
    <div class="menu-item"><div class="item-head"><span>Grilled Atlantic Salmon Salad</span><span class="item-price">$9.99 - $12.99</span></div><p class="item-desc">A charbroiled salmon filet seasoned to perfection on a bed of fresh romaine lettuce topped with shredded parmesan cheese, tomatoes, and croutons.</p><p class="item-sizes"><span>Small</span>$9.99 <b>Large</b> $12.99</p></div>
    <div class="menu-item"><div class="item-head"><span>Sirloin Salad</span><span class="item-price">$9.99 - $12.99</span></div><p class="item-desc">Saute'ed slices of choice sirloin atop a bed of fresh romaine lettuce, tossed with tomatoes, parmesan cheese and croutons.</p><p class="item-sizes"><span>Small</span>$9.99 <b>Large</b> $12.99</p></div>
  </div>

  <div class="entree-list">
    <p class="section-note">All Entrees are served with your choice of side and garlic bread.</p>
    <div class="menu-item"><div class="item-head"><span>Chicken Strip Basket</span><span class="item-price">$5.99 - $8.99</span></div><p class="item-desc">Our classic chicken tenders served with your choice of side and dipping sauce.</p><p class="item-sizes" style="margin-top:1px"><span>Small</span>$5.99 <b>Large</b> $8.99</p></div>
    <div class="menu-item"><div class="item-head"><span>Grilled Chicken Breast Fillet</span><span class="item-price">$7.99 - $10.99</span></div><p class="item-desc">A classic boneless, skinless chicken breast brushed with a bourbon peppercorn glaze.</p><p class="item-sizes"><span>Small</span>$7.99 <b>Large</b> $10.99</p></div>
    <div class="menu-item" style="margin-bottom:17px"><div class="item-head"><span>Blackened Tilapia</span><span class="item-price">$10.99</span></div><p class="item-desc">8 oz. grilled tilapia filet, blackened and served with your choice of side.</p></div>
    <div class="menu-item"><div class="item-head"><span>Deep Fried Catfish</span><span class="item-price">$7.99 - $10.99</span></div><p class="item-desc">A classic boneless, skinless chicken breast brushed with a bourbon peppercorn glaze.</p><p class="item-sizes"><span>Small</span>$7.99 <b>Large</b> $10.99</p></div>
    <div class="menu-item"><div class="item-head"><span>Pepper Jack Burger Steak</span><span class="item-price">$7.99 - $10.99</span></div><p class="item-desc">A 12oz. ground beef patty smothered in melted pepper jack cheese and jalapeño peppers.</p><p class="item-sizes"><span>Small</span>$7.99 <b>Large</b> $10.99</p></div>
    <div class="menu-item"><div class="item-head"><span>St. Louie Ribs</span><span class="item-price">$13.99 - $17.99</span></div><p class="item-desc">A three pound slab of slow roasted barbecue glazed ribs.</p><p class="item-sizes" style="margin-top:2px"><span>Half Rack</span>$13.99 &nbsp;<b>Full Rack</b> $17.99</p></div>
    <div class="menu-item"><div class="item-head"><span>Pork Stuffed Baked Potato</span><span class="item-price">$8.99</span></div><p class="item-desc">Buttered and salted baked potato stuffed with a mountain of BBQ pulled pork, Cheddar and Jack cheese, blooming onion petals, sour cream and green onions. Served with a side salad.</p></div>
    <div class="menu-item"><div class="item-head"><span>Harborview Loaded Chicken</span><span class="item-price">$9.99 - $12.99</span></div><p class="item-desc">Our grilled chicken breast piled high with melted jack and cheddar cheese, sautéed onions and mushrooms, crisp bacon, and honey mustard.</p><p class="item-sizes" style="margin-top:1px"><span>Small</span>$9.99 <b>Large</b> $12.99</p></div>
    <div class="menu-item"><div class="item-head"><span>Chicken Fried Chicken Dinner</span><span class="item-price">$9.99</span></div><p class="item-desc">Crispy chicken breast smothered in country gravy served with your choice of side and steamed vegetables.</p></div>
    <div class="menu-item"><div class="item-head"><span>Fried Shrimp</span><span class="item-price">$7.99 - $10.99</span></div><p class="item-desc">A plate full of lightly breaded butterflied shrimp served with cocktail sauce.</p><p class="item-sizes"><span>Small</span>$7.99 <b>Large</b> $10.99</p></div>
  </div>
</section>

<section class="menu-column col-right">
  <div class="steak-list">
    <div class="menu-item"><div class="item-head"><span>Country Fried Steak</span><span class="item-price">$7.99 - $10.99</span></div><p class="item-desc">Hand breaded and deep fried, smothered in old fashioned country gravy.</p><p class="item-sizes" style="margin-top:2px"><span>Small</span>$7.99 <b>Large</b> $10.99</p></div>
    <div class="menu-item"><div class="item-head"><span>Black N' Blue Sirloin</span><span class="item-price">$15.99</span></div><p class="item-desc">12 oz. choice cut sirloin cooked to your request, blackened and topped with melted blue cheese crumbles.</p></div>
    <div class="menu-item"><div class="item-head"><span>Iron Griddle Steak</span><span class="item-price">$14.99</span></div><p class="item-desc">12 oz. aged and cut from the strip loin. Cooked to your request.</p></div>
    <div class="menu-item"><div class="item-head"><span>Flat Iron Steak</span><span class="item-price">$16.99</span></div><p class="item-desc">9 oz. flat iron seasoned and cooked to your request.</p></div>
  </div>

  <div class="sandwich-list">
    <p class="section-note">All sandwiches are served with your choice of side dish.</p>
    <div class="menu-item"><div class="item-head"><span>Harborview Club Sandwich</span><span class="item-price">$9.99</span></div><p class="item-desc">Layers of ham, turkey, roast beef, bacon and cheese. Served with mayo on a toasted focaccia bun</p></div>
    <div class="menu-item"><div class="item-head"><span>Chicken Breast Sandwich</span><span class="item-price">$7.99</span></div><p class="item-desc">Choice of crispy or grilled chicken breast, lettuce, tomato and pickles. Served with mayo on a toasted bun.</p></div>
    <div class="menu-item"><div class="item-head"><span>Bang Bang Turkey Wrap</span><span class="item-price">$7.99</span></div><p class="item-desc">A grilled 12 inch tortilla stuffed with roasted turkey breast, mozzarella cheese, lettuce and our spicy bang bang sauce.</p></div>
    <div class="menu-item"><div class="item-head"><span>Roast Beef &amp; Cheddar</span><span class="item-price">$7.99</span></div><p class="item-desc">Thinly sliced slow cooked roast beef smothered with a cheddar cheese sauces on a ciabatta bun. Served with spicy BBQ sauce.</p></div>
    <div class="menu-item"><div class="item-head"><span>B.L.T.</span><span class="item-price">$6.99</span></div><p class="item-desc">This classic bacon, lettuce and tomato sandwich is served with mayo on your choice of white, wheat or sourdough toast.</p></div>
    <div class="menu-item"><div class="item-head"><span>Hank's Spicy Buffalo Chicken Sandwich</span><span class="item-price">$8.99</span></div><p class="item-desc">Crispy fried chicken breast smothered in Hank's Spicy Buffalo sauce. Served on a ciabatta bun. Dressed with jalapeño ranch, lettuce, tomato and pickle.</p></div>
    <div class="menu-item"><div class="item-head"><span>Triple Decker Reuben</span><span class="item-price">$7.99</span></div><p class="item-desc">Layer after layer of grilled corned beef, sauerkraut, swiss cheese and Thousand Island dressing. Served on toasted Rye.</p></div>
    <div class="menu-item"><div class="item-head"><span>Classic French Dip</span><span class="item-price">$8.99</span></div><p class="item-desc">Thinly sliced roast beef grilled and loaded with Swiss cheese and grilled onions. Served with French onion soup.</p></div>
    <div class="menu-item"><div class="item-head"><span>Crispy Chicken Bacon Ranch Wrap</span><span class="item-price">$8.99</span></div><p class="item-desc">A 12 inch grilled tortilla stuffed with crispy chicken tenders, bacon, lettuce, tomatoes and ranch dressing.</p></div>
    <div class="menu-item"><div class="item-head"><span>Southern Style Pulled Pork</span><span class="item-price">$7.99</span></div><p class="item-desc">Smoked pulled pork smothered in tangy barbecue sauce on a toasted hoagie. Served with cole slaw on request</p></div>
    <div class="menu-item"><div class="item-head"><span>Chicken Fry Steak Sandwich</span><span class="item-price">$7.99</span></div><p class="item-desc">Hand breaded chicken fried steak topped with bacon, lettuce, pickles, tomato and onion.</p></div>
    <div class="menu-item"><div class="item-head"><span>Philly Steak &amp; Cheese Sandwich</span><span class="item-price">$7.99</span></div><p class="item-desc">Thinly sliced steak piled high with melted monterey jack cheese, grilled onions and peppers on a toasted hoagie.</p></div>
    <div class="menu-item"><div class="item-head"><span>Eight Cheese Grilled Cheese</span><span class="item-price">$7.99</span></div><p class="item-desc">Taking this classic to the Gourmet level! Eight cheeses melted thick on toasted sourdough bread.</p></div>
    <div class="menu-item"><div class="item-head"><span>Chicken Cordon Bleu Sandwich</span><span class="item-price">$8.99</span></div><p class="item-desc">your choice of crispy or grilled chicken breast layered with grilled ham, swiss cheese, lettuce, tomatoes and pickles. Served with mayo on a toasted bun.</p></div>
  </div>
</section>
</body>
</html>
```